Napa Winery - Chardonnay wine label

We are looking for a label for a new Napa Valley winery - chardonnay wine. The winery is "Marrowbrook Hill Vintners" and we would like to see it depicted on a white wine (chardonnay style) bottle. The winery is called Marrowbrook Hill Vintners.

We are open to ideas!

Target Market(s)

High-end chardonnay lovers

Requirements
Nice to have
• Painted or etched label onto bottle

```html
<!DOCTYPE html>
<html lang="en">
<head>
<meta charset="utf-8">
<title>Quiet Providence Chardonnay – Label</title>
<link rel="stylesheet" href="https://fonts.googleapis.com/css2?family=Varela+Round&family=Comfortaa:wght@300;400&display=swap">
<style>
  :root {
    --page-bg: #ffffff;
    --label-paper: #fdfbf5;
    --label-edge: #ece8de;
    --title-ink: #545454;
    --varietal-green: #2f9a3f;
    --caption-ink: #6a6a6a;
    --feather-light: #f1f1f1;
    --feather-mid: #b9b9b9;
    --feather-dark: #5e5e5e;
  }
  * { box-sizing: border-box; margin: 0; padding: 0; }
  html, body {
    width: 1114px;
    height: 1200px;
    overflow: hidden;
    background: var(--page-bg);
  }
  .wine-label {
    position: absolute;
    left: 107px;
    top: 170px;
    width: 900px;
    height: 860px;
    background: var(--label-paper);
    border: 1px solid var(--label-edge);
  }
  .wine-name {
    position: absolute;
    left: 0;
    right: 0;
    top: 56px;
    padding-left: 70px;
    text-align: center;
    font-family: "Varela Round", sans-serif;
    font-weight: 400;
    font-size: 96px;
    line-height: 0.98;
    letter-spacing: -1px;
    color: var(--title-ink);
  }
  .varietal {
    position: absolute;
    left: 0;
    right: 0;
    top: 300px;
    padding-left: 10px;
    text-align: center;
    font-family: "Comfortaa", sans-serif;
    font-weight: 300;
    font-size: 54px;
    color: var(--varietal-green);
  }
  .feather-art {
    position: absolute;
    left: 190px;
    top: 470px;
    width: 560px;
    height: 150px;
    border-radius: 50%;
    transform: rotate(-20deg);
    background: linear-gradient(90deg, var(--feather-mid) 0%, var(--feather-light) 55%, var(--feather-dark) 100%);
    opacity: 0.8;
  }
  .winery-credit {
    position: absolute;
    left: 0;
    right: 0;
    top: 752px;
    text-align: center;
    font-family: "Varela Round", sans-serif;
    font-size: 28px;
    line-height: 50px;
    letter-spacing: 0.5px;
    color: var(--caption-ink);
  }
</style>
</head>
<body>
  <main class="wine-label">
    <h1 class="wine-name">Quiet<br>Providence</h1>
    <p class="varietal">Chardonnay</p>
    <div class="feather-art" role="img" aria-label="Etched grey feather illustration drifting diagonally across the label"></div>
    <p class="winery-credit">Napa Valley Winery<br>Marrowbrook Hill Vintners</p>
  </main>
</body>
</html>
```